New Store Open for Business

Glow with Mirela is a beauty supply store online at www.glowwithmirela.net and we have just opened our brick n mortar store in Essex.

The leaflet is to promote and attract clients to our new business in the area, and to inform them of our specialist service in Afro and European Hair care.
Our location:

31-35 Wexcombe Lane
Grays
Essex
RM14 3TN

tel: 01375 482917
website: www.glowwithmirela.net

Hours of operation:
Mon - Sat: 0900 - 2000
Sun: 1000 - 1900

As well as haircare products, we also sell wigs, extensions and hair pieces, accessories, and skincare products.

The copy for the flyer:

At Glow with Mirela you’ll find old favourites and amazing new brands.
Come and visit our new Essex branch today and relax knowing that you have finally found your one-stop beauty shop!

HAIR CARE
WIGS
EXTENSIONS
HAIR PIECES
SKIN CARE
ACCESSORIES
HEALTH

Our location:

31-35 Wexcombe Lane
Grays
Essex
RM14 3TN

tel: 01375 482917

Hours of operation:
Mon - Sat: 0900 - 2000
Sun: 1000 - 1900

the logo should take a prominent position

Social media platforms:
Facebook: Glow with Mirela
Twitter; @GlowWith_Mirela
Instagram: glow_with_mirela
Pinterest: Glow with Mirela

Haircare has been corrected to Hair Care Skincare has been corrected to Skin Care

Target Market(s)

Young black women primarily

Industry/Entity Type

Store

Font styles to use
Sans Serif

Requirements
Must have
• At Glow with Mirela you’ll find old favourites and amazing new brands.

HAIR CARE
WIGS
EXTENSIONS
HAIR PIECES
SKIN CARE
ACCESSORIES
HEALTH

Our location:

31-35 Wexcombe Lane
Grays
Essex
RM14 3TN

tel: 01375 482917

Hours of operation:
Mon - Sat: 0900 - 2000
Sun: 1000 - 1900
Nice to have
• Black models (hair model)

```html
<!DOCTYPE html>
<html lang="en">
<head>
<meta charset="utf-8">
<title>Glow with Mirela – New Beauty Supply Store Leaflet</title>
<link rel="stylesheet" href="https://fonts.googleapis.com/css2?family=Jost:wght@300;400;500;600;700&display=swap">
<style>
  :root {
    --pink: #e5007d;
    --black: #0b0b0b;
    --white: #ffffff;
    --gap: #ffffff;
    --skin-dark: #3a2118;
    --skin-mid: #7a4a34;
    --hair: #1a100c;
  }
  * { box-sizing: border-box; margin: 0; padding: 0; }
  html, body { width: 1200px; height: 423px; overflow: hidden; background: var(--gap); }
  body { font-family: "Jost", "Futura", Arial, sans-serif; color: var(--white); position: relative; }

  .leaflet { position: absolute; top: 0; height: 423px; background: var(--black); overflow: hidden; }
  .leaflet--front { left: 0; width: 597px; }
  .leaflet--back { left: 605px; width: 595px; }

  .hero-model {
    position: absolute; left: 330px; top: 0; width: 267px; height: 378px;
    background:
      radial-gradient(ellipse 60% 45% at 62% 40%, var(--skin-mid), transparent 70%),
      radial-gradient(ellipse 70% 60% at 75% 85%, #6b3d2a, transparent 70%),
      radial-gradient(ellipse 55% 80% at 30% 55%, var(--hair), transparent 80%),
      linear-gradient(90deg, var(--black), var(--skin-dark) 55%, #241410);
  }

  .web-address {
    position: absolute; top: 13px; font-size: 14px; font-weight: 400; letter-spacing: 3.4px; color: var(--white);
  }
  .leaflet--front .web-address { left: 362px; }
  .leaflet--back .web-address { left: 360px; }

  .brand { position: absolute; top: 24px; font-weight: 300; color: var(--white); text-align: center; line-height: 1; }
  .brand__small { display: block; font-size: 17px; letter-spacing: 6.5px; }
  .brand__large { display: block; font-size: 44px; letter-spacing: 6px; margin-top: 6px; }
  .leaflet--front .brand { left: 78px; }
  .leaflet--back .brand { left: 63px; }

  .intro {
    position: absolute; left: 36px; top: 97px; width: 320px; font-size: 13.5px; line-height: 17.5px; font-weight: 400;
  }

  .model-thumbs { position: absolute; left: 34px; top: 176px; display: flex; gap: 24px; }
  .model-thumb {
    width: 90px; height: 90px; border-radius: 50%;
    border: 3px dotted var(--pink); padding: 3px;
  }
  .model-thumb span { display: block; width: 100%; height: 100%; border-radius: 50%; }
  .model-thumb:nth-child(1) span { background: radial-gradient(circle at 45% 40%, #8a5a44, #2c1a14 75%); }
  .model-thumb:nth-child(2) span { background: radial-gradient(circle at 50% 45%, #e8d2b6, #b58e63 75%); }
  .model-thumb:nth-child(3) span { background: radial-gradient(circle at 55% 45%, #a56a4c, #4a2a1d 75%); }

  .visit { position: absolute; left: 33px; top: 272px; }
  .leaflet--back .visit { left: 31px; }
  .visit__lead { font-size: 14px; font-weight: 600; letter-spacing: 0.3px; line-height: 1; }
  .visit__title { font-size: 22.5px; font-weight: 600; color: var(--pink); line-height: 1; margin-top: 2px; letter-spacing: 0.2px; }
  .visit__phone { display: flex; align-items: center; gap: 8px; margin-top: 11px; font-size: 22px; font-weight: 600; line-height: 1; letter-spacing: 0.5px; }
  .visit__phone svg { width: 30px; height: 24px; }
  .visit__address { font-size: 14px; font-weight: 400; margin-top: 10px; line-height: 1; }

  .social-band { position: absolute; left: 0; bottom: 0; width: 100%; height: 45px; background: var(--pink); }
  .social-item {
    position: absolute; top: 15px; display: flex; align-items: center; gap: 6px; font-size: 14px; font-weight: 400; line-height: 1;
  }
  .social-item::before { content: ""; width: 10px; height: 10px; background: var(--white); display: block; }

  .services-heading {
    position: absolute; left: 31px; top: 114px; font-size: 12.5px; font-weight: 600; display: flex; align-items: center; gap: 3px;
  }
  .services-heading::after { content: ""; width: 135px; height: 1.5px; background: var(--white); display: block; }

  .services {
    position: absolute; left: 31px; top: 132px; width: 270px;
    display: grid; grid-template-columns: 102px 22px auto; row-gap: 2px;
    color: var(--pink); font-size: 19px; font-weight: 600; line-height: 25px;
  }
  .services .left { text-align: right; }
  .services .dot { display: flex; align-items: center; justify-content: center; }
  .services .dot::before { content: ""; width: 9px; height: 9px; border-radius: 50%; background: var(--white); }
  .services .row-gap { grid-column: 1 / 4; height: 3px; }

  .hours { position: absolute; left: 0; top: 0; width: 595px; height: 240px; pointer-events: none; }

  .client-thumb {
    position: absolute; left: 466px; top: 68px; width: 66px; height: 66px; border-radius: 50%;
    border: 2px solid var(--white);
    background: radial-gradient(circle at 45% 45%, #8a5a40, #2a1a14 70%);
  }

  .storefront { position: absolute; left: 370px; top: 177px; width: 225px; height: 201px; }
  .storefront svg { width: 100%; height: 100%; display: block; }
</style>
</head>
<body>

<section class="leaflet leaflet--front">
  <div class="hero-model" role="img" aria-label="Large photo of a model with long glossy dark wavy hair"></div>

  <div class="web-address">www.glowwithmirela.net</div>

  <div class="brand">
    <span class="brand__small">Glow with</span>
    <span class="brand__large">Mirela</span>
  </div>

  <p class="intro">At Glow with Mirela you’ll find old favourites and amazing new brands. Come and visit our new Essex branch today and relax knowing that you have finally found your one-stop beauty shop!</p>

  <div class="model-thumbs">
    <div class="model-thumb"><span role="img" aria-label="Portrait photo of a hair model with dark hair"></span></div>
    <div class="model-thumb"><span role="img" aria-label="Portrait photo of a hair model with long blonde hair"></span></div>
    <div class="model-thumb"><span role="img" aria-label="Portrait photo of a hair model with a short auburn bob"></span></div>
  </div>

  <div class="visit">
    <div class="visit__lead">VISIT OUR</div>
    <div class="visit__title">NEW BEAUTY SUPPLY STORE</div>
    <div class="visit__phone">
      <svg viewBox="0 0 30 24" aria-hidden="true">
        <path d="M2 8 C2 3 28 3 28 8 L28 10 L21 10 L21 7 C18 6 12 6 9 7 L9 10 L2 10 Z" fill="none" stroke="#fff" stroke-width="2" stroke-linejoin="round"/>
        <path d="M9 11 L21 11 L26 22 L4 22 Z" fill="none" stroke="#fff" stroke-width="2" stroke-linejoin="round"/>
        <circle cx="15" cy="16.5" r="3" fill="none" stroke="#fff" stroke-width="1.8"/>
      </svg>
      <span>01375 482917</span>
    </div>
    <div class="visit__address">31-35 Wexcombe Lane, Grays, Essex, RM14 3TN</div>
  </div>

  <div class="social-band">
    <span class="social-item" style="left:36px">Glow with Mirela</span>
    <span class="social-item" style="left:165px">@GlowWith_Mirela</span>
    <span class="social-item" style="left:312px">Glow with Mirela</span>
    <span class="social-item" style="left:460px">glow_with_mirela</span>
  </div>
</section>

<section class="leaflet leaflet--back">
  <div class="web-address">www.glowwithmirela.net</div>

  <div class="brand">
    <span class="brand__small">Glow with</span>
    <span class="brand__large">Mirela</span>
  </div>

  <div class="services-heading">OUR SERVICES</div>
  <div class="services">
    <span class="left">HAIR CARE</span><span class="dot"></span><span>EXTENSIONS</span>
    <span class="left">WIGS</span><span class="dot"></span><span>HAIR PIECES</span>
    <span class="row-gap"></span>
    <span class="left">SKIN CARE</span><span class="dot"></span><span>ACCESSORIES</span>
    <span class="left">HEALTH</span><span class="dot"></span><span>MAKE-UP</span>
  </div>

  <div class="storefront">
    <svg viewBox="0 0 225 201" preserveAspectRatio="none" role="img" aria-label="Photo of the shop front with its fascia sign and window displays">
      <defs>
        <linearGradient id="storefront-tone" x1="0" y1="0" x2="0" y2="1">
          <stop offset="0" stop-color="#2b3f7a"/>
          <stop offset="0.35" stop-color="#253566"/>
          <stop offset="0.4" stop-color="#4a3b46"/>
          <stop offset="1" stop-color="#6c6a73"/>
        </linearGradient>
      </defs>
      <polygon points="0,68 225,0 225,201 0,201" fill="url(#storefront-tone)"/>
    </svg>
  </div>

  <svg class="hours" viewBox="0 0 595 240" role="group" aria-label="Opening times">
    <defs>
      <path id="hours-arc" d="M 321 110 A 80 80 0 0 1 453 100"/>
    </defs>
    <text font-family="Jost, sans-serif" font-size="17" font-weight="600" fill="#fff" letter-spacing="1">
      <textPath href="#hours-arc">OPENING TIMES</textPath>
    </text>
    <circle cx="390" cy="150" r="66" fill="#e5007d" stroke="#fff" stroke-width="4"/>
    <g font-family="Jost, sans-serif" font-weight="600" fill="#fff" text-anchor="middle">
      <text x="390" y="118" font-size="19">MON - SAT</text>
      <text x="390" y="142" font-size="19">0900 - 2000</text>
      <text x="390" y="162" font-size="19">SUN</text>
      <text x="390" y="181" font-size="18">1000 - 1900</text>
    </g>
    <circle cx="462" cy="55" r="9" fill="#e5007d"/>
    <circle cx="448" cy="43" r="5" fill="#e5007d"/>
    <circle cx="483" cy="158" r="9" fill="#e5007d"/>
    <circle cx="470" cy="176" r="5" fill="#e5007d"/>
  </svg>

  <div class="client-thumb" role="img" aria-label="Photo of a customer with voluminous natural afro hair"></div>

  <div class="visit">
    <div class="visit__lead">VISIT OUR</div>
    <div class="visit__title">NEW BEAUTY SUPPLY STORE</div>
    <div class="visit__phone">
      <svg viewBox="0 0 30 24" aria-hidden="true">
        <path d="M2 8 C2 3 28 3 28 8 L28 10 L21 10 L21 7 C18 6 12 6 9 7 L9 10 L2 10 Z" fill="none" stroke="#fff" stroke-width="2" stroke-linejoin="round"/>
        <path d="M9 11 L21 11 L26 22 L4 22 Z" fill="none" stroke="#fff" stroke-width="2" stroke-linejoin="round"/>
        <circle cx="15" cy="16.5" r="3" fill="none" stroke="#fff" stroke-width="1.8"/>
      </svg>
      <span>01375 482917</span>
    </div>
    <div class="visit__address">31-35 Wexcombe Lane, Grays, Essex, RM14 3TN</div>
  </div>

  <div class="social-band">
    <span class="social-item" style="left:35px">Glow with Mirela</span>
    <span class="social-item" style="left:162px">@GlowWith_Mirela</span>
    <span class="social-item" style="left:311px">Glow with Mirela</span>
    <span class="social-item" style="left:460px">glow_with_mirela</span>
  </div>
</section>

</body>
</html>
```